Wedding Dried Apple Label / Name Place Card

We are looking for a simple but stylish label to be attached via string to a bag of dried apples from my family's fruit farm. The size of the label we think should be similar to the size of a business card. The packaging will be a plastic bag: 4" x 2" x 6".
We would like it to say something like:
Remy & Joss
Est. Sept 10, 2017
Dried Apple Slices
Product of Quenton Fruit Farm
________________
(We need a spot to write in the name of the person and a table number)
Our colors are also grey and navy, and would like these colors to be used.
We have uploaded a photo of the plastic bag.
Wedding

```html
<!DOCTYPE html>
<html lang="en">
<head>
<meta charset="utf-8">
<title>Remy &amp; Joss – Dried Apple Slices Label</title>
<link rel="stylesheet" href="https://fonts.googleapis.com/css2?family=Arimo:wght@400;700&display=swap">
<style>
  :root {
    --navy: #2d2d62;
    --grey-text: #a6a6a6;
    --card: #ffffff;
    --page: #e4e3dc;
    --sketch-light: #f3f3f3;
    --sketch-mid: #d9d9d9;
  }
  * { margin: 0; padding: 0; box-sizing: border-box; }
  html, body {
    width: 1200px;
    height: 795px;
    overflow: hidden;
    background: var(--page);
    font-family: "Arimo", Arial, sans-serif;
  }
  .label {
    position: absolute;
    left: 100px;
    top: 147px;
    width: 1000px;
    height: 500px;
    background: var(--card);
    box-shadow: 0 6px 18px rgba(0, 0, 0, 0.12);
  }
  .label__brand {
    position: absolute;
    left: 67px;
    top: 50px;
    font-size: 66px;
    font-weight: 400;
    color: var(--navy);
    letter-spacing: -0.5px;
    line-height: 1;
  }
  .label__band {
    position: absolute;
    left: 0;
    top: 170px;
    width: 694px;
    height: 159px;
  }
  .label__band svg { display: block; }
  .label__title {
    position: absolute;
    left: 67px;
    top: 27px;
    font-size: 52px;
    font-weight: 700;
    color: #fff;
    line-height: 1;
  }
  .label__origin {
    position: absolute;
    left: 67px;
    top: 92px;
    font-size: 35px;
    font-weight: 400;
    color: #fff;
    line-height: 1;
  }
  .label__sketch {
    position: absolute;
    left: 640px;
    top: 50px;
    width: 330px;
    height: 370px;
    border-radius: 50%;
    background: radial-gradient(ellipse at 55% 45%, var(--sketch-light) 0%, var(--sketch-mid) 100%);
  }
  .label__write-line {
    position: absolute;
    left: 0;
    top: 459px;
    width: 694px;
    height: 2px;
    background: var(--navy);
  }
  .label__est {
    position: absolute;
    left: 706px;
    top: 440px;
    font-size: 30px;
    color: var(--grey-text);
    line-height: 1;
  }
</style>
</head>
<body>
  <div class="label">
    <div class="label__brand">Remy &amp; Joss</div>

    <div class="label__band">
      <svg width="694" height="159" viewBox="0 0 694 159" aria-hidden="true">
        <path d="M0 0 H694 Q656 80 694 159 H0 Z" fill="var(--navy)"/>
      </svg>
      <div class="label__title">Dried Apple Slices</div>
      <div class="label__origin">Product of Quenton Fruit Farm</div>
    </div>

    <div class="label__sketch" role="img" aria-label="Black ink sketch of a halved apple with a leaf and a slice"></div>

    <div class="label__write-line"></div>
    <div class="label__est">Est. Sept 10, 2017</div>
  </div>
</body>
</html>
```